" SOU MÉDICO ORTOPEDISTA COM ESPECIALIZAÇÃO EM CIRURGIA DO JOELHO E DO QUADRIL. REALIZO ATENDIMENTOS AMBULATORIAIS E CIRURGICOS NESTAS ARÉAS PRINCIPALMENTE. "

```html
<!DOCTYPE html>
<html lang="pt-BR">
<head>
<meta charset="utf-8">
<title>Pasta institucional – Marcelo de Andrade Sousa</title>
<link rel="stylesheet" href="https://fonts.googleapis.com/css2?family=Montserrat:wght@400;500&display=swap">
<style>
  :root {
    --backdrop: #ecebe8;
    --paper: #ffffff;
    --navy-deep: #0d2238;
    --navy: #123f63;
    --navy-light: #1b5a84;
    --accent-blue: #2f7fcf;
    --ink-grey: #8a96a3;
    --ink-light: #d8e3ee;
    --shadow: rgba(0, 0, 0, 0.22);
  }
  * { margin: 0; padding: 0; box-sizing: border-box; }
  html, body {
    width: 1200px;
    height: 1200px;
    overflow: hidden;
    background: var(--backdrop);
    font-family: "Montserrat", sans-serif;
  }
  .folder {
    position: absolute;
    left: 163px;
    top: 220px;
    width: 874px;
    height: 830px;
  }
  .folder-inside {
    position: absolute;
    left: 0;
    top: 0;
    width: 461px;
    height: 830px;
    overflow: visible;
  }
  .folder-cover {
    position: absolute;
    left: 461px;
    top: 0;
    width: 413px;
    height: 790px;
    background: linear-gradient(90deg, var(--navy-deep) 0%, var(--navy) 55%, var(--navy-light) 100%);
    box-shadow: 4px 6px 14px var(--shadow);
  }
  .identity {
    position: absolute;
    display: flex;
    flex-direction: column;
    align-items: center;
    text-align: center;
  }
  .identity-mark {
    width: 46px;
    height: 46px;
    border-radius: 50%;
    margin-bottom: 14px;
  }
  .identity-name {
    font-weight: 400;
    font-size: 17px;
    letter-spacing: 0.6px;
    white-space: nowrap;
  }
  .identity-specialty {
    font-weight: 500;
    font-size: 8.5px;
    letter-spacing: 2.2px;
    margin-top: 5px;
    white-space: nowrap;
  }
  .identity--inside {
    left: 0;
    width: 461px;
    top: 168px;
  }
  .identity--inside .identity-mark { border: 3px solid var(--ink-grey); }
  .identity--inside .identity-name { color: var(--ink-grey); }
  .identity--inside .identity-specialty { color: var(--accent-blue); }
  .identity--cover {
    left: 0;
    width: 413px;
    top: 176px;
  }
  .identity--cover .identity-mark { border: 3px solid var(--ink-light); }
  .identity--cover .identity-name { color: var(--ink-light); }
  .identity--cover .identity-specialty { color: var(--ink-light); }
</style>
</head>
<body>
  <main class="folder">
    <svg class="folder-inside" viewBox="0 0 461 830" width="461" height="830" aria-hidden="true">
      <defs>
        <linearGradient id="band-gradient" x1="0" x2="1" y1="0" y2="0">
          <stop offset="0" stop-color="#1a3d7a"/>
          <stop offset="0.7" stop-color="#2f7fcf"/>
          <stop offset="1" stop-color="#5aa8ec"/>
        </linearGradient>
      </defs>
      <rect class="inside-panel" x="0" y="0" width="461" height="790" fill="#ffffff"/>
      <path class="pocket-flap" d="M0 596 H418 C418 700 360 790 250 830 H0 Z" fill="#ffffff" stroke="#dcdcdc" stroke-width="1"/>
      <rect class="pocket-band" x="0" y="592" width="418" height="12" fill="url(#band-gradient)"/>
    </svg>
    <div class="identity identity--inside">
      <span class="identity-mark"></span>
      <span class="identity-name">MARCELO DE ANDRADE SOUSA</span>
      <span class="identity-specialty">ORTOPEDIA E TRAUMATOLOGIA</span>
    </div>

    <section class="folder-cover">
      <div class="identity identity--cover">
        <span class="identity-mark"></span>
        <span class="identity-name">MARCELO DE ANDRADE SOUSA</span>
        <span class="identity-specialty">ORTOPEDIA E TRAUMATOLOGIA</span>
      </div>
    </section>
  </main>
</body>
</html>
```